Business Card Design Project

We need a business card design for a relatively new company called Velmar Gear. We design paddle (an outdoor winter sport primarily played in the midwest and east coast) and tennis bags for women and men. Velmar Gear is a lifestyle brand for the next generation country club goers. Our bags merge fashion with functionality and are making country club sports trendier and more fashionable.

I would like to include space for
Name: (will fill this in for employees)
Velmar Gear
Phone: (will do this)
Email:
www.velmargear.example

Would also like to include Chatterbook and Flitter icons.
Please do not use pictures of the bags - this is just to give you an idea of what style bags we sell.

Target Market(s)

30 to 40 year old men and women - luxury market

Industry/Entity Type

Fashion

Requirements
Must have
• Would like the company logo included

```html
<!DOCTYPE html>
<html lang="en">
<head>
<meta charset="utf-8">
<title>Velmar Gear – Business Card</title>
<link rel="stylesheet" href="https://fonts.googleapis.com/css2?family=Questrial&family=Open+Sans:wght@400;700&display=swap">
<style>
  :root {
    --orange: #f7873a;
    --orange-deep: #d9641c;
    --orange-text: #e0772d;
    --ink: #111111;
    --paper: #ffffff;
    --paper-shade: #e9e9e9;
    --stage: #2b2b2b;
  }
  * { box-sizing: border-box; margin: 0; padding: 0; }
  html, body { width: 1200px; height: 900px; overflow: hidden; }
  body {
    background: var(--stage);
    font-family: "Open Sans", sans-serif;
    position: relative;
  }
  .card {
    position: absolute;
    left: 250px;
    width: 700px;
    height: 400px;
    overflow: hidden;
    box-shadow: 0 10px 30px rgba(0,0,0,0.5);
  }
  /* Back side */
  .card-back {
    top: 35px;
    background: var(--orange);
    display: flex;
    align-items: center;
    justify-content: center;
    gap: 22px;
  }
  .card-back .mark-dot {
    width: 70px; height: 70px; border-radius: 50%;
    background: var(--orange-deep);
  }
  .card-back .back-name {
    font-family: "Questrial", sans-serif;
    font-size: 64px;
    color: var(--orange-deep);
  }
  /* Front side */
  .card-front {
    top: 465px;
    background: linear-gradient(100deg, var(--paper) 40%, var(--paper-shade) 100%);
  }
  .accent-band {
    position: absolute; left: 0; top: 0;
    width: 130px; height: 100%;
    background: var(--orange);
  }
  .brand {
    position: absolute; left: 95px; top: 48px;
    display: flex; align-items: center; gap: 16px;
  }
  .brand-dot {
    width: 52px; height: 52px; border-radius: 50%;
    background: var(--ink);
  }
  .brand-name {
    font-family: "Questrial", sans-serif;
    font-size: 62px;
    color: var(--ink);
    line-height: 1;
  }
  .contact {
    position: absolute; right: 36px; top: 130px;
    text-align: right;
    color: var(--orange-text);
  }
  .contact-name {
    font-weight: 700; font-size: 22px; letter-spacing: 0.5px;
    text-transform: uppercase;
  }
  .contact-role { font-size: 14px; margin-top: -2px; }
  .contact-rule {
    width: 190px; height: 1.5px; background: var(--orange-text);
    margin: 8px 0 8px auto;
  }
  .contact-line { font-size: 16px; line-height: 1.35; }
  .social {
    display: flex; justify-content: flex-end; gap: 12px;
    margin-top: 14px;
    font-size: 12px;
  }
  .social-item { display: flex; align-items: center; gap: 5px; }
  .social-item::before {
    content: ""; width: 14px; height: 14px; background: var(--orange-text);
  }
  .website {
    position: absolute; right: 36px; bottom: 26px;
    font-size: 20px; color: var(--orange-text);
  }
</style>
</head>
<body>
  <section class="card card-back" aria-label="Card back">
    <span class="mark-dot"></span>
    <span class="back-name">Velmar Gear</span>
  </section>

  <section class="card card-front" aria-label="Card front">
    <div class="accent-band"></div>
    <div class="brand">
      <span class="brand-dot"></span>
      <span class="brand-name">Velmar Gear</span>
    </div>
    <div class="contact">
      <p class="contact-name">Dana Corvel</p>
      <p class="contact-role">Founder</p>
      <div class="contact-rule"></div>
      <p class="contact-line">P: 555.014.2323</p>
      <p class="contact-line">F: 555.014.4343</p>
      <p class="contact-line">dana@velmargear.example</p>
      <div class="social">
        <span class="social-item">Flitter</span>
        <span class="social-item">Chatterbook</span>
      </div>
    </div>
    <p class="website">www.velmargear.example</p>
  </section>
</body>
</html>
```